Business Card for Auto Dealership - Clean, sharp and professional

Please use the maroon logo with the grey background. Need a sharp, clean and professional business card for an Auto Dealer. In the files provides there is three different logos. I have not decided which one to go with yet. Right now I am favoring the grey/silver background. I would like my contact info on there and the website as well. I feel like less is more and want something simple, clean and sharp. Thank you in advance for your tie and effort! I also need email signature, letterhead, etc after this

Target Market(s)

Car buyers

Industry/Entity Type

Automotive

Contact Information for Business Card

Drew
555-214-7730
www.BriarvaleAutoLink.example
Drew@BriarvaleAutoLink.example

Font styles to use
Serif
Sans Serif

Requirements
Must have
• Please use the maroon logo with the grey background. Business Card Details and logo from files. Please stick to the logo colors

```html
<!DOCTYPE html>
<html lang="en">
<head>
<meta charset="UTF-8">
<title>Briarvale Auto Link – Business Card</title>
<link href="https://fonts.googleapis.com/css2?family=Montserrat:wght@400;500;600&display=swap" rel="stylesheet">
<style>
  :root {
    --canvas: #ffffff;
    --card: #e7e9eb;
    --maroon: #5a1c1c;
    --band: #4e1414;
    --text: #5a1c1c;
  }
  * { margin: 0; padding: 0; box-sizing: border-box; }
  html, body {
    width: 1200px; height: 627px; overflow: hidden;
    background: var(--canvas);
    font-family: "Montserrat", Arial, sans-serif;
  }
  .canvas { position: relative; width: 1200px; height: 627px; }

  .card {
    position: absolute; top: 153px;
    width: 482px; height: 278px;
    background: var(--card);
    overflow: hidden;
  }
  .card--front { left: 67px; }
  .card--back  { left: 603px; }
  .card__band {
    position: absolute; left: 0; right: 0; top: 224px; height: 29px;
    background: var(--band);
  }

  .brand { position: absolute; display: flex; align-items: center; color: var(--maroon); }
  .brand__dot { flex: none; border-radius: 50%; border: solid var(--maroon); }
  .brand__name { font-weight: 600; line-height: 1; white-space: nowrap; }
  .brand__name span { display: block; }

  .card--front .brand { left: 70px; top: 68px; }
  .card--front .brand__dot { width: 88px; height: 88px; border-width: 7px; margin-right: 26px; }
  .card--front .brand__name .line-1 { font-size: 33px; letter-spacing: 2px; }
  .card--front .brand__name .line-2 { font-size: 12.5px; letter-spacing: 7.4px; margin-top: 6px; }

  .card--back .brand { left: 7px; top: 102px; }
  .card--back .brand__dot { width: 54px; height: 54px; border-width: 5px; margin-right: 10px; }
  .card--back .brand__name .line-1 { font-size: 17px; letter-spacing: 1px; }
  .card--back .brand__name .line-2 { font-size: 7px; letter-spacing: 3.4px; margin-top: 4px; }

  .person {
    position: absolute; right: 20px; top: 10px;
    font-size: 44px; font-weight: 500; line-height: 1.2; color: var(--text);
  }
  .contact { position: absolute; left: 218px; top: 80px; list-style: none; }
  .contact__item {
    display: flex; align-items: center;
    height: 18px; margin-bottom: 21px;
    font-size: 12px; color: var(--text);
    white-space: nowrap;
  }
  .contact__icon { width: 14px; height: 14px; margin-right: 9px; flex: none; fill: var(--maroon); }
</style>
</head>
<body>
<main class="canvas">

  <section class="card card--front">
    <div class="brand">
      <div class="brand__dot"></div>
      <div class="brand__name"><span class="line-1">BRIARVALE</span><span class="line-2">AUTO LINK</span></div>
    </div>
    <div class="card__band"></div>
  </section>

  <section class="card card--back">
    <h1 class="person">Drew</h1>
    <div class="brand">
      <div class="brand__dot"></div>
      <div class="brand__name"><span class="line-1">BRIARVALE</span><span class="line-2">AUTO LINK</span></div>
    </div>
    <ul class="contact">
      <li class="contact__item">
        <svg class="contact__icon" viewBox="0 0 24 24"><path d="M6.6 10.8c1.4 2.8 3.8 5.1 6.6 6.6l2.2-2.2c.3-.3.7-.4 1-.2 1.1.4 2.3.6 3.6.6.6 0 1 .4 1 1V20c0 .6-.4 1-1 1C10.6 21 3 13.4 3 4c0-.6.4-1 1-1h3.5c.6 0 1 .4 1 1 0 1.3.2 2.5.6 3.6.1.3 0 .7-.2 1z"/></svg>
        555-214-7730
      </li>
      <li class="contact__item">
        <svg class="contact__icon" viewBox="0 0 24 24"><path d="M12 2a10 10 0 1 0 0 20 10 10 0 0 0 0-20zm6.9 6h-2.9a15.6 15.6 0 0 0-1.4-3.6A8 8 0 0 1 18.9 8zM12 4c.8 1.2 1.5 2.5 1.9 4h-3.8c.4-1.5 1.1-2.8 1.9-4zM4.3 14a8.2 8.2 0 0 1 0-4h3.4a16.5 16.5 0 0 0 0 4H4.3zm.8 2h2.9c.3 1.3.8 2.5 1.4 3.6A8 8 0 0 1 5.1 16zM8 8H5.1a8 8 0 0 1 4.3-3.6C8.8 5.5 8.3 6.7 8 8zm4 12c-.8-1.2-1.5-2.5-1.9-4h3.8c-.4 1.5-1.1 2.8-1.9 4zm2.3-6H9.7a14.7 14.7 0 0 1 0-4h4.6a14.7 14.7 0 0 1 0 4zm.3 5.6c.6-1.1 1.1-2.3 1.4-3.6h2.9a8 8 0 0 1-4.3 3.6zm1.7-5.6a16.5 16.5 0 0 0 0-4h3.4a8.2 8.2 0 0 1 0 4h-3.4z"/></svg>
        www.BriarvaleAutoLink.example
      </li>
      <li class="contact__item">
        <svg class="contact__icon" viewBox="0 0 24 24"><path d="M2 5h20v14H2V5zm2 2v.5l8 5 8-5V7H4zm0 2.8V17h16V9.8l-8 5-8-5z"/></svg>
        Drew@BriarvaleAutoLink.example
      </li>
    </ul>
    <div class="card__band"></div>
  </section>

</main>
</body>
</html>
```